KARATE Enrollment Postcard Design

We provide professional karate tuition for all ages 6+
I need a design that will appeal to children and parents alike.
Needs to emphasise fun & fitness as well as self defence and confidence - anti bully.

There are a lot of bad franchise clubs in the area with really high prices that teach rubbish, which tend to go big on advertising and are therefore expensive.
We are a small family business that teach Karate properly (white suits) and compete at world level.
Karate seems no have fell behind MMA in terms of popularity although we teach all aspects of the sport ie grappling / padwork / kata / sparring.

Need to make Karate EXCITING again!

I need to run a promotion to encourage new members maybe £25 a months tuition?

Needs to stand out to parents/adults when dropped through a letter box but be 'cool' enough for kids to give to there friends.

Reason: Not quite found what in looking for yet.

Target Market(s)

kids age 6+ and general Adults

Industry/Entity Type

Advertising

```html
<!DOCTYPE html>
<html lang="en">
<head>
<meta charset="utf-8">
<title>Karate Enrollment Postcard</title>
<link href="https://fonts.googleapis.com/css2?family=Fjalla+One&family=Roboto:wght@400;700&display=swap" rel="stylesheet">
<style>
  :root {
    --bg: #e9e6e1;
    --black: #0c0c0c;
    --red: #d3231c;
    --white: #ffffff;
    --wood-dark: #3b2f27;
    --wood-light: #7a6a5c;
    --gold: #e2b64a;
    --gold-dark: #a97d1c;
    --line: #9a9a9a;
  }
  * { margin: 0; padding: 0; box-sizing: border-box; }
  html, body { width: 793px; height: 1200px; overflow: hidden; background: var(--bg); }
  body { position: relative; font-family: "Roboto", Arial, sans-serif; }

  .card {
    position: absolute; left: 66px; width: 661px; overflow: hidden;
    box-shadow: 0 4px 14px rgba(0,0,0,.35);
  }
  .card--front { top: 40px; height: 535px; background: var(--black); }
  .card--back { top: 610px; height: 555px; background: var(--white); }

  .front__sun {
    position: absolute; left: 222px; top: 24px; width: 400px; height: 400px;
    border-radius: 50%; background: var(--red);
  }
  .front__wood {
    position: absolute; left: 0; right: 0; top: 330px; bottom: 0;
    background: linear-gradient(180deg, var(--wood-light), var(--wood-dark));
  }
  .front__fighters {
    position: absolute; left: 240px; top: 90px; width: 350px; height: 300px;
    background: linear-gradient(160deg, #1a1a1a, #000);
    border-radius: 46% 54% 40% 60% / 50% 40% 60% 50%;
    opacity: .85;
  }
  .brand {
    position: absolute; left: 24px; top: 24px;
    font-family: "Fjalla One", "Arial Narrow", sans-serif;
    color: var(--white); font-size: 26px; line-height: 1.15;
    display: flex; align-items: center; gap: 10px;
  }
  .brand__dot { width: 14px; height: 14px; border-radius: 50%; background: var(--white); flex: none; }
  .front__headline {
    position: absolute; left: 0; right: 0; top: 410px; text-align: center;
    font-family: "Fjalla One", "Arial Narrow", sans-serif;
    color: var(--white); font-size: 46px; line-height: 1.08;
    text-shadow: 3px 3px 0 var(--black);
  }

  .back__panel {
    position: absolute; left: 0; top: 0; width: 330px; height: 100%;
    background: var(--black); overflow: hidden;
  }
  .back__title {
    position: absolute; left: 22px; top: 26px;
    font-family: "Fjalla One", "Arial Narrow", sans-serif;
    color: var(--white); font-size: 38px;
  }
  .back__circle {
    position: absolute; left: -20px; top: 110px; width: 370px; height: 370px;
    border-radius: 50%; background: var(--red);
  }
  .back__copy {
    position: absolute; left: 40px; top: 135px; width: 250px;
    color: var(--white); font-size: 13px; font-weight: 700; line-height: 1.3;
    text-align: center;
  }
  .back__copy p { margin-bottom: 14px; }
  .offer {
    position: absolute; left: 35px; top: 470px; width: 260px; height: 44px;
  }
  .offer__text {
    position: absolute; inset: 0; display: flex; align-items: center; justify-content: center;
    font-family: "Fjalla One", "Arial Narrow", sans-serif;
    font-size: 20px; color: var(--black);
  }
  .stamp {
    position: absolute; left: 450px; top: 72px; width: 56px; height: 66px;
    border: 2px solid var(--black);
  }
  .address-line {
    position: absolute; left: 360px; width: 270px; height: 0;
    border-top: 1.5px solid var(--line);
  }
</style>
</head>
<body>

<section class="card card--front">
  <div class="front__sun"></div>
  <div class="front__wood" role="img" aria-label="Weathered wood texture"></div>
  <div class="front__fighters" role="img" aria-label="Silhouettes of two karate fighters, one performing a high kick"></div>
  <div class="brand">
    <span class="brand__dot"></span>
    <span>Kaizen-ryu<br>Karate</span>
  </div>
  <h1 class="front__headline">Teaching Self Esteem<br>through Self Defence</h1>
</section>

<section class="card card--back">
  <div class="back__panel">
    <div class="back__circle"></div>
    <h2 class="back__title">BULLY PROOF</h2>
    <div class="back__copy">
      <p>We provide professional karate tuition for all ages 6+.</p>
      <p>There are a lot of bad franchise clubs in the area with really high prices that teach rubbish, which tend to go big on advertising and are therefore expensive.</p>
      <p>We are a small family business that teach Karate properly (white suits) and compete at world level. Karate seems no have fell behind MMA in terms of popularity although we teach all aspects of the sport in grappling / padwork / kata / sparring.</p>
    </div>
    <div class="offer">
      <svg width="260" height="44" viewBox="0 0 260 44" aria-hidden="true">
        <polygon points="0,10 22,10 22,40 0,40 10,25" fill="var(--gold-dark)"/>
        <polygon points="260,10 238,10 238,40 260,40 250,25" fill="var(--gold-dark)"/>
        <rect x="14" y="2" width="232" height="34" fill="var(--gold)"/>
      </svg>
      <div class="offer__text">£25 A MONTHS TUITION</div>
    </div>
  </div>
  <div class="stamp"></div>
  <div class="address-line" style="top:300px"></div>
  <div class="address-line" style="top:330px"></div>
  <div class="address-line" style="top:360px"></div>
  <div class="address-line" style="top:390px"></div>
</section>

</body>
</html>
```